I would like a flyer for the ultimate masquarade ball. This will be a PARTY! We need a flyer that will jump out and catch the attention of anyone who sees it. We would like plenty of purple and gold to be used in the flyer. The final design should communicate the ultmate, upscale, classy, exciting masquarade ball ever!

This flyer must be designed for high resolution for printing on 4" x 6" flyers.

Requirements
Must have
• Zeta Kappa Chapter Presents
Lantern Velvet & Ember MasQUErade Ball
1 March 2014
8pm - 1am
3-Course Plated Dinner
Cash Bar
RSVP By: 28 Feb 2014
Halvorsen Gaming & Downs, North Banquet Hall
DJ Tavrik
Details & Tickets: http://lanternvelvetemberball.ticketnook.example
More Info? 555-318-7726
Dress Code: Black Tie & Traditional Dress, Costumes & Masks Preferred

```html
<!DOCTYPE html>
<html lang="en">
<head>
<meta charset="utf-8">
<title>Lantern Velvet &amp; Ember Masquerade Ball</title>
<link rel="stylesheet" href="https://fonts.googleapis.com/css2?family=Cinzel:wght@400;700&family=Kaushan+Script&family=Dancing+Script:wght@700&family=Open+Sans:wght@600;700;800&family=PT+Sans:wght@400;700&display=swap">
<style>
  :root {
    --ink: #050307;
    --gold: #f3d27a;
    --gold-soft: #f6dc8c;
    --gold-bar: #f5d676;
    --cream: #fbf4e2;
    --white: #ffffff;
    --grey: #c8c8c8;
    --bar-text: #4a1460;
  }
  html, body {
    margin: 0;
    padding: 0;
    width: 851px;
    height: 1200px;
    overflow: hidden;
    background: var(--ink);
  }
  .flyer {
    position: relative;
    width: 851px;
    height: 1200px;
    overflow: hidden;
    background: var(--ink);
    font-family: "Open Sans", Arial, sans-serif;
    color: var(--white);
  }
  .mask-art {
    position: absolute;
    inset: 0;
    background:
      radial-gradient(ellipse 380px 300px at 560px 200px, rgba(182,69,214,0.85), rgba(110,30,140,0.55) 55%, transparent 80%),
      radial-gradient(ellipse 300px 260px at 760px 420px, rgba(120,40,150,0.55), transparent 75%),
      radial-gradient(ellipse 260px 220px at 120px 120px, rgba(90,20,120,0.45), transparent 75%),
      linear-gradient(180deg, #1a0622 0%, #0c0410 55%, var(--ink) 75%);
  }
  .line {
    position: absolute;
    left: 0;
    width: 100%;
    margin: 0;
    text-align: center;
    white-space: nowrap;
  }
  .presents {
    top: 8px;
    font-weight: 700;
    font-size: 23px;
  }
  .event-name {
    top: 84px;
    font-family: "Cinzel", Georgia, serif;
    font-weight: 700;
    font-size: 31px;
    letter-spacing: 11px;
    color: var(--gold);
  }
  .event-title {
    top: 116px;
    font-family: "Cinzel", Georgia, serif;
    font-weight: 400;
    font-size: 77px;
    letter-spacing: 1px;
    color: var(--cream);
  }
  .title-rule {
    position: absolute;
    left: 128px;
    top: 204px;
    width: 600px;
    height: 2px;
    background: linear-gradient(90deg, transparent, var(--white) 20%, var(--white) 80%, transparent);
  }
  .flourish {
    position: absolute;
    left: 320px;
    top: 206px;
    width: 210px;
    height: 64px;
    border-radius: 50%;
    background: radial-gradient(ellipse at center, rgba(255,255,255,0.35), transparent 70%);
  }
  .venue {
    font-weight: 800;
    font-size: 34px;
    color: var(--gold);
    letter-spacing: 0.5px;
  }
  .venue-1 { top: 302px; }
  .venue-2 { top: 350px; }
  .date-time {
    top: 402px;
    font-weight: 700;
    font-size: 28px;
    color: var(--gold);
  }
  .photo-row {
    position: absolute;
    left: 30px;
    top: 466px;
  }
  .photo-label {
    font-family: "Open Sans", Arial, sans-serif;
    font-weight: 600;
    font-size: 56px;
    fill: var(--grey);
  }
  .dj {
    top: 752px;
    font-family: "Kaushan Script", "Dancing Script", cursive;
    font-size: 66px;
    color: var(--gold);
  }
  .amenity {
    font-family: "PT Sans", Arial, sans-serif;
    font-size: 35px;
    color: var(--gold-soft);
  }
  .dinner { top: 876px; }
  .bar { top: 938px; }
  .swoosh {
    position: absolute;
    left: 0;
    top: 930px;
  }
  .corner-mask {
    position: absolute;
    left: 0;
    top: 1000px;
    width: 200px;
    height: 130px;
    background: radial-gradient(ellipse at 40% 50%, rgba(200,120,230,0.45), transparent 70%);
  }
  .small-flourish {
    position: absolute;
    left: 382px;
    top: 1002px;
    width: 86px;
    height: 18px;
    border-radius: 50%;
    background: radial-gradient(ellipse at center, rgba(255,255,255,0.6), transparent 72%);
  }
  .rsvp {
    top: 1030px;
    font-weight: 700;
    font-size: 18px;
    color: var(--cream);
  }
  .dress-heading {
    top: 1068px;
    font-weight: 800;
    font-size: 20px;
    letter-spacing: 1px;
    color: var(--gold);
  }
  .dress-detail {
    top: 1097px;
    font-weight: 700;
    font-size: 21px;
  }
  .info-bar {
    position: absolute;
    left: 0;
    top: 1133px;
    width: 851px;
    height: 67px;
    background: var(--gold-bar);
    color: var(--bar-text);
    font-family: "PT Sans", Arial, sans-serif;
    font-size: 19px;
    text-align: center;
    line-height: 40px;
    white-space: nowrap;
  }
  .info-bar strong { font-weight: 700; }
</style>
</head>
<body>
<div class="flyer">
  <div class="mask-art" role="img" aria-label="Purple glittering masquerade mask photograph fading into black"></div>

  <p class="line presents">Zeta Kappa Chapter Presents...</p>
  <h1 class="line event-name">LANTERN VELVET &amp; EMBER</h1>
  <p class="line event-title">MASQUERADE BALL</p>
  <div class="title-rule"></div>
  <div class="flourish" role="img" aria-label="White decorative flourish"></div>

  <p class="line venue venue-1">HALVORSEN GAMING &amp; DOWNS</p>
  <p class="line venue venue-2">NORTH BANQUET HALL</p>
  <p class="line date-time">1 March 2014 &nbsp;•&nbsp; 8pm - 1am</p>

  <svg class="photo-row" width="791" height="222" viewBox="0 0 791 222" role="img" aria-label="Four overlapping circular photo frames">
    <g fill="#ffffff" stroke="#d9b24a" stroke-width="5">
      <circle cx="110" cy="111" r="105"/>
      <circle cx="301" cy="111" r="105"/>
      <circle cx="491" cy="111" r="105"/>
      <circle cx="681" cy="111" r="105"/>
    </g>
    <g fill="#ffffff">
      <circle cx="110" cy="111" r="102"/>
      <circle cx="301" cy="111" r="102"/>
      <circle cx="491" cy="111" r="102"/>
      <circle cx="681" cy="111" r="102"/>
    </g>
    <text class="photo-label" x="398" y="133" text-anchor="middle">images</text>
  </svg>

  <p class="line dj">DJ Tavrik</p>
  <p class="line amenity dinner">3-Course Plated Dinner</p>

  <svg class="swoosh" width="851" height="203" viewBox="0 0 851 203" aria-hidden="true">
    <defs>
      <linearGradient id="swooshFill" x1="0" y1="0" x2="1" y2="0">
        <stop offset="0" stop-color="#3a0a4f"/>
        <stop offset="0.5" stop-color="#6a1d8c"/>
        <stop offset="1" stop-color="#b645d6"/>
      </linearGradient>
    </defs>
    <path d="M0 40 Q 420 120 851 0 L851 203 L0 203 Z" fill="url(#swooshFill)"/>
    <path d="M0 40 Q 420 120 851 0" fill="none" stroke="#d98cf0" stroke-width="2" opacity="0.7"/>
  </svg>
  <div class="corner-mask" role="img" aria-label="Faint purple masquerade mask image"></div>

  <p class="line amenity bar">Cash Bar</p>
  <div class="small-flourish" role="img" aria-label="Small white flourish"></div>
  <p class="line rsvp">RSVP By: 28 Feb 2014</p>

  <p class="line dress-heading">DRESS CODE</p>
  <p class="line dress-detail">Black Tie &amp; Traditional Dress • Costumes &amp; Masks Preferred</p>

  <div class="info-bar">
    <strong>More Info?</strong> 555-318-7726 • <strong>Details &amp; Tickets:</strong> lanternvelvetemberball.ticketnook.example
  </div>
</div>
</body>
</html>
```